BenQoral Medical

We are a medical supplier company we sell machines and equipment to all medical sectors in Iraq. Our services include not only the installation of these machines and equipment but also we provide support after installation and we train the staff to use these machines/equipment
We need a website that will make us stand out from our competitors, something professional and catchy
Starting from the home page, before showing the home page we want the loading screen to have our logo animated in a nice way
Then we can proceed to creating the other pages which are
Projects
Services
Training
About
and Contact us
Attached below is our logo and the color blue that we hope to use in the theme of the website
**** In the home page we want to focus on our partners and services****

Target Market(s)

Medical Sector

Industry/Entity Type

Medical

Coding

Coded - Design and coding required

Number of Pages Required

5+ page

Colors
0054AA
0677BA
7BADD7
CADEEF
E8F1F8

Requirements
Must have
• Animation in loading screen or animation in home page
Nice to have
• Some sort of animation for our partners

```html
<!DOCTYPE html>
<html lang="en">
<head>
<meta charset="UTF-8">
<title>BenQoral Medical</title>
<link href="https://fonts.googleapis.com/css2?family=Montserrat:wght@500;600;700;800&family=Poppins:wght@400;500;600&display=swap" rel="stylesheet">
<style>
:root{
  --navy:#1b1f5e;
  --navy-deep:#151949;
  --blue:#1a8fd8;
  --band:#1e9be0;
  --ink:#1b1f5e;
  --text:#4a4f66;
  --muted:#8a8fa3;
  --card:#e9e9ea;
  --field:#eef0f3;
  --white:#ffffff;
  --footer-text:#d5d8ea;
  --star:#f5a623;
}
*{margin:0;padding:0;box-sizing:border-box}
html,body{width:1200px;height:4256px;overflow:hidden}
body{position:relative;font-family:"Poppins",sans-serif;color:var(--text);background:var(--white)}
h1,h2,h3,h4,.brand{font-family:"Montserrat",sans-serif}
.abs{position:absolute}
.btn{display:inline-block;background:var(--blue);color:#fff;font-family:"Poppins",sans-serif;font-size:15px;font-weight:500;padding:12px 26px;border-radius:3px}
.photo{background:linear-gradient(160deg,#dfe6ee,#9fb1c4);}

/* header / hero */
.hero{left:0;top:0;width:1200px;height:780px;background:var(--navy)}
.brand{display:flex;align-items:center;gap:10px;color:#fff;font-size:26px;font-weight:700;white-space:nowrap}
.brand .mark{width:30px;height:30px;border:3px solid #fff;border-radius:3px;flex:none}
.nav{right:88px;top:22px;display:flex;align-items:center;gap:26px}
.nav a{color:#fff;font-size:14px;text-decoration:none}
.nav .btn{padding:10px 22px;font-size:14px}
.hero-title{left:0;width:1200px;top:192px;text-align:center;color:#fff;font-size:50px;font-weight:700;line-height:1.2}
.hero-sub{left:0;width:1200px;top:322px;text-align:center;color:#dfe3f5;font-size:15px}
.strip{left:-14px;top:380px;display:flex;gap:12px}
.strip div{width:236px;height:290px}
.dots{display:flex;gap:8px;justify-content:center}
.dots span{width:9px;height:9px;border-radius:50%;background:#7b80b5}
.dots span.on{background:#fff}
.contact-chip{display:flex;align-items:center;gap:14px;color:#fff;font-size:15px}
.contact-chip .ic{width:40px;height:40px;border-radius:50%;background:#fff;display:flex;align-items:center;justify-content:center}

/* insurance band */
.band{left:0;top:800px;width:1200px;height:90px;background:var(--band);display:flex;align-items:center;padding:0 60px;gap:46px}
.band .label{color:#fff;font-size:18px;font-style:italic;font-family:"Montserrat",sans-serif;font-weight:500;white-space:nowrap}
.band .partner{height:22px;border-radius:4px;background:rgba(255,255,255,.85)}

/* section headings */
.eyebrow{color:var(--blue);font-size:16px;font-weight:500}
.heading{color:var(--ink);font-size:34px;font-weight:700;line-height:1.25}
.center{left:0;width:1200px;text-align:center}

/* services */
.svc-img{left:88px;top:1112px;width:480px;height:480px}
.svc-grid{left:592px;top:1112px;width:520px;display:grid;grid-template-columns:1fr 1fr;gap:12px}
.svc-card{background:var(--card);height:234px;padding:20px 18px;text-align:center}
.svc-card svg{width:40px;height:40px}
.svc-card h3{color:var(--ink);font-size:17px;font-weight:700;margin:8px 0 8px}
.svc-card p{font-size:12px;line-height:1.55;color:#5a5f73}

/* about */
.about-text{left:88px;top:1830px;width:430px}
.about-text p{font-size:13px;line-height:1.7;margin-top:16px}
.about-img{left:620px;top:1808px;width:492px;height:384px}
.stat{background:#fff;box-shadow:0 8px 26px rgba(20,30,80,.15);text-align:center;padding-top:34px;height:200px}
.stat b{display:block;font-family:"Montserrat",sans-serif;color:var(--blue);font-size:50px;font-weight:700}
.stat span{color:var(--ink);font-size:15px;font-weight:500}

/* equipment */
.equip{left:0;top:2228px;width:1200px;height:492px;background:var(--navy)}
.equip-row{left:88px;top:2348px;width:1024px;display:flex;gap:16px}
.equip-card{width:192px;height:304px;background:#fff}
.equip-card .photo{height:252px;margin:6px;background:linear-gradient(180deg,#f6f7f9,#c9d0d9)}
.equip-card p{text-align:center;color:var(--ink);font-size:15px;font-weight:500;margin-top:8px}

/* testimonials */
.quote-card{width:440px}
.quote-card .q{font-family:"Montserrat",sans-serif;color:var(--ink);font-size:46px;line-height:1;font-weight:800;position:absolute;left:-40px;top:-6px}
.quote-card p{font-size:15px;line-height:1.75;color:#555a6e}
.author{display:flex;align-items:center;gap:12px;margin-top:24px;color:var(--ink);font-size:14px;font-weight:500}
.author .av{width:40px;height:40px;border-radius:50%;background:#c7ccd6}
.stars{color:var(--star);letter-spacing:2px}

/* cta / form */
.cta-bg{left:0;top:3280px;width:1200px;height:500px;background:#f5f6fa}
.cta-mark{left:88px;top:3390px;width:96px;height:96px;border:10px solid var(--ink);border-radius:6px}
.form{left:540px;top:3280px;width:580px;height:480px;background:#fff;box-shadow:0 10px 40px rgba(20,30,80,.14);padding:40px 42px}
.form .row{display:grid;grid-template-columns:1fr 1fr;gap:22px;margin-bottom:18px}
.form label{display:block;color:var(--ink);font-size:13px;font-weight:500;margin-bottom:6px}
.field{height:44px;background:var(--field);border-radius:3px;padding:0 12px;display:flex;align-items:center;color:#a3a8b8;font-size:12px}
.field.area{height:88px;align-items:flex-start;padding-top:12px}

/* footer */
.footer{left:0;top:3780px;width:1200px;height:420px;background:var(--navy)}
.footer .brand{left:88px;top:200px;font-size:21px}
.footer .brand .mark{width:28px;height:28px}
.footer .social{left:92px;top:262px}
.footer-col{top:48px}
.footer-col.links{left:340px;width:170px}
.footer-col.contact{left:552px;width:230px}
.footer-col.news{left:820px;width:292px}
.footer h4{color:#fff;font-size:22px;font-weight:700;margin-bottom:16px;white-space:nowrap}
.footer ul{list-style:none}
.footer li{color:var(--footer-text);font-size:14px;line-height:1.9}
.footer li .k{color:#fff;font-weight:500}
.footer .news p{color:var(--footer-text);font-size:13px;line-height:1.6;margin-bottom:18px}
.social{display:flex;gap:12px}
.social span{width:34px;height:34px;border-radius:50%;border:1.5px solid #fff}
.sub-input{width:280px;height:44px;background:#fff;border-radius:3px;display:flex;align-items:center;justify-content:space-between;padding:0 6px 0 14px;color:#9aa0b2;font-size:13px}
.sub-input span{width:34px;height:34px;background:var(--blue);border-radius:3px;display:flex;align-items:center;justify-content:center}
.copy{left:0;top:4200px;width:1200px;height:56px;background:var(--navy-deep);color:var(--footer-text);font-size:13px;display:flex;align-items:center;justify-content:center}
</style>
</head>
<body>

<!-- hero -->
<header class="abs hero"></header>
<div class="abs brand" style="left:88px;top:16px"><span class="mark"></span>BenQoral Medical</div>
<nav class="abs nav">
  <a href="#">Home</a><a href="#">About Us</a><a href="#">Projects</a><a href="#">Services</a><a href="#">Training</a>
  <span class="btn">Contact Us</span>
</nav>
<h1 class="abs hero-title">Leading The Future Of<br>Medical Equipment and Support</h1>
<p class="abs hero-sub">Empowering Healthcare Facilities with Cutting-Edge Medical Technology and Unmatched Support.</p>
<div class="abs strip">
  <div class="photo" role="img" aria-label="Hospital operating room with medical equipment"></div>
  <div class="photo" role="img" aria-label="Modern hospital ward with patient beds"></div>
  <div class="photo" role="img" aria-label="Surgical suite with overhead lights"></div>
  <div class="photo" role="img" aria-label="Imaging room with scanner"></div>
  <div class="photo" role="img" aria-label="Intensive care room with monitors"></div>
</div>
<div class="abs dots center" style="top:708px"><span class="on"></span><span></span><span></span><span></span></div>
<div class="abs contact-chip" style="left:88px;top:726px">
  <span class="ic"><svg width="20" height="20" viewBox="0 0 24 24"><path fill="#1b1f5e" d="M6.6 10.8a15 15 0 0 0 6.6 6.6l2.2-2.2c.3-.3.7-.4 1-.2 1.1.4 2.3.6 3.6.6.6 0 1 .4 1 1V20c0 .6-.4 1-1 1A17 17 0 0 1 3 4c0-.6.4-1 1-1h3.5c.6 0 1 .4 1 1 0 1.3.2 2.5.6 3.6.1.3 0 .7-.2 1z"/></svg></span>
  +964 770 555 0192
</div>
<div class="abs contact-chip" style="right:88px;top:726px">
  <span class="ic"><svg width="20" height="20" viewBox="0 0 24 24"><path fill="#1b1f5e" d="M3 5h18v14H3z M4 6l8 6 8-6" stroke="#fff" stroke-width="1.4"/></svg></span>
  support@benqoral.com
</div>

<!-- partners band -->
<div class="abs band">
  <span class="label">Insurance Accepted</span>
  <span class="partner" style="width:92px"></span>
  <span class="partner" style="width:120px"></span>
  <span class="partner" style="width:80px"></span>
  <span class="partner" style="width:96px"></span>
  <span class="partner" style="width:100px"></span>
  <span class="partner" style="width:104px"></span>
</div>

<!-- services -->
<p class="abs eyebrow center" style="top:990px">Our Services</p>
<h2 class="abs heading center" style="top:1018px">Comprehensive Medical Solutions<br>for Every Sector</h2>
<div class="abs photo svc-img" role="img" aria-label="Patient lying on an MRI scanner table"></div>
<div class="abs svc-grid">
  <div class="svc-card">
    <svg viewBox="0 0 40 40" fill="none" stroke="#1b1f5e" stroke-width="2"><rect x="6" y="10" width="28" height="22" rx="2"/><path d="M14 10V6h12v4M20 16v10M15 21h10"/></svg>
    <h3>Equipment Supply</h3>
    <p>We offer a wide range of medical devices and machinery, carefully selected to meet the diverse needs of hospitals, clinics, and other healthcare facilities.</p>
  </div>
  <div class="svc-card">
    <svg viewBox="0 0 40 40" fill="none" stroke="#1b1f5e" stroke-width="2"><circle cx="20" cy="20" r="7"/><path d="M20 5v6M20 29v6M5 20h6M29 20h6M9 9l4 4M27 27l4 4M31 9l-4 4M13 27l-4 4"/></svg>
    <h3>Professional Installation</h3>
    <p>Our team ensures that all equipment is installed with precision and efficiency, minimizing downtime and disruption to your services.</p>
  </div>
  <div class="svc-card">
    <svg viewBox="0 0 40 40" fill="none" stroke="#1b1f5e" stroke-width="2"><path d="M8 22a12 12 0 0 1 24 0"/><rect x="6" y="22" width="6" height="9" rx="2"/><rect x="28" y="22" width="6" height="9" rx="2"/><path d="M31 31c0 3-4 4-9 4"/></svg>
    <h3>Ongoing Support</h3>
    <p>We provide continuous support to address any issues that arise, ensuring that your equipment operates smoothly and efficiently.</p>
  </div>
  <div class="svc-card">
    <svg viewBox="0 0 40 40" fill="none" stroke="#1b1f5e" stroke-width="2"><rect x="5" y="7" width="30" height="20" rx="1"/><path d="M20 27v6M13 33h14M11 21l6-6 4 4 8-8"/></svg>
    <h3>Comprehensive Training</h3>
    <p>Our experts offer detailed training sessions to your staff, empowering them to maximize the benefits of the technology.</p>
  </div>
</div>
<span class="abs btn" style="left:548px;top:1660px">Read More</span>

<!-- about -->
<div class="abs about-text">
  <p class="eyebrow" style="margin:0">About Us</p>
  <h2 class="heading" style="font-size:34px;margin-top:4px">Who We Are</h2>
  <p>Founded with a vision to elevate medical standards, we specialize in supplying state-of-the-art medical machines and equipment to various sectors within the healthcare industry. Our commitment extends beyond just providing equipment; we are your partners in ensuring that these tools are seamlessly integrated into your operations and that your staff is fully equipped to utilize them effectively.</p>
  <span class="btn" style="margin-top:24px">Read More</span>
</div>
<div class="abs photo about-img" role="img" aria-label="Row of modern medical imaging machines"></div>
<div class="abs stat" style="left:552px;top:1888px;width:168px"><b>75+</b><span>Rooms Available</span></div>
<div class="abs stat" style="left:730px;top:1888px;width:176px"><b>63</b><span>Medical Staffs</span></div>

<!-- featured equipment -->
<section class="abs equip"></section>
<h2 class="abs heading center" style="top:2284px;color:#fff">Featured Equipment</h2>
<div class="abs equip-row">
  <div class="equip-card"><div class="photo" role="img" aria-label="Anesthesia machine"></div><p>Anesthia</p></div>
  <div class="equip-card"><div class="photo" role="img" aria-label="Ventilator unit"></div><p>Ventilator</p></div>
  <div class="equip-card"><div class="photo" role="img" aria-label="Endoscopy tower"></div><p>Endoscopy</p></div>
  <div class="equip-card"><div class="photo" role="img" aria-label="Neurosurgery microscope"></div><p>Neurosurgery</p></div>
  <div class="equip-card"><div class="photo" role="img" aria-label="Contrast dye injector"></div><p>Dye Injector</p></div>
</div>
<span class="abs btn" style="left:508px;top:2664px">View All Equipment</span>

<!-- testimonials -->
<p class="abs eyebrow center" style="top:2812px">Testimonials</p>
<h2 class="abs heading center" style="top:2840px">What Do Happy Clients Say About<br>Working With Us?</h2>
<div class="abs quote-card" style="left:160px;top:2956px">
  <span class="q">&ldquo;</span>
  <p>Their team not only provided top-of-the-line machines but also offered outstanding support and training. Their commitment to excellence is evident in every interaction. Their team's expertise and support have been crucial in ensuring that our staff is proficient in using the new technology.</p>
  <div class="author"><span class="av"></span>Layla K <span class="stars">★★★★★</span></div>
</div>
<div class="abs quote-card" style="left:640px;top:2956px">
  <span class="q">&ldquo;</span>
  <p>Their team not only provided top-of-the-line machines but also offered outstanding support and training. Their commitment to excellence is evident in every interaction. Their team's expertise and support have been crucial in ensuring that our staff is proficient in using the new technology.</p>
  <div class="author"><span class="av"></span>Omar &amp; Huda S <span class="stars">★★★★★</span></div>
</div>
<div class="abs dots center" style="top:3228px"><span style="background:#1b1f5e"></span><span style="background:#c6cade"></span><span style="background:#c6cade"></span><span style="background:#c6cade"></span></div>

<!-- cta -->
<div class="abs cta-bg"></div>
<div class="abs cta-mark"></div>
<h2 class="abs heading" style="left:88px;top:3514px;font-size:34px;line-height:1.2">Let's Start Your<br>Transformation<br>Journey</h2>
<p class="abs" style="left:88px;top:3650px;width:340px;font-size:14px;line-height:1.6">Complete the form below to schedule your meeting with Consultancy Business</p>
<form class="abs form">
  <div class="row">
    <div><label>First Name*</label><div class="field">First Name</div></div>
    <div><label>Last Name*</label><div class="field">Last Name</div></div>
  </div>
  <div class="row">
    <div><label>email*</label><div class="field">Email Address</div></div>
    <div><label>company*</label><div class="field">Company</div></div>
  </div>
  <label>message*</label>
  <div class="field area">Type your questions</div>
  <div style="text-align:center;margin-top:26px"><span class="btn">schedule demo</span></div>
</form>

<!-- footer -->
<footer class="abs footer">
  <div class="abs brand"><span class="mark"></span>BenQoral Medical</div>
  <div class="abs social"><span></span><span></span><span></span><span></span></div>
  <div class="abs footer-col links">
    <h4>Quick Link</h4>
    <ul><li>Home</li><li>Projects</li><li>Services</li><li>Training</li><li>About</li><li>Contact Us</li></ul>
  </div>
  <div class="abs footer-col contact">
    <h4>Contact Us</h4>
    <ul>
      <li><span class="k">Phone</span><br>+964 770 555 0192</li>
      <li><span class="k">Email</span><br>support@benqoral.com</li>
      <li><span class="k">Address</span><br>42 Karrada Street,<br>Baghdad, Iraq</li>
    </ul>
  </div>
  <div class="abs footer-col news">
    <h4>Subscribe Newsletter</h4>
    <p>Subscribe newsletter for the latest offers and news</p>
    <div class="sub-input">Enter your email<span><svg width="16" height="16" viewBox="0 0 24 24"><path fill="#fff" d="M2 21l21-9L2 3v7l15 2-15 2z"/></svg></span></div>
  </div>
</footer>
<div class="abs copy">Copyrights 2024. All Rights Reserved</div>

</body>
</html>
```